Website Design for Employee Moral and Happiness Company

Looking for a clean website design that explains our features in a step by step manner so our visitors know exactly what our site does before logging in.

The site is called "Velasto". See logo design and video for a sample of style and an overview of what we do.

Target Market(s)

Business owners that are looking to retain employees.

Number of Pages Required

1 page

```html
<!DOCTYPE html>
<html lang="en">
<head>
<meta charset="utf-8">
<title>Velasto — Employee Morale &amp; Happiness</title>
<link href="https://fonts.googleapis.com/css2?family=Jost:wght@400;500;600&family=Roboto+Slab:wght@300;400;600;700&display=swap" rel="stylesheet">
<style>
:root{
  --orange:#f26522;
  --orange-light:#ff8a3d;
  --orange-deep:#f0530f;
  --ink:#141414;
  --text:#555;
  --muted:#888;
  --hero-bg:#f1f0f0;
  --white:#fff;
  --footer:#0b0b0b;
  --footer-bar:#1c1c1c;
}
*{margin:0;padding:0;box-sizing:border-box}
html,body{width:1200px;height:4222px;overflow:hidden}
body{position:relative;background:var(--white);font-family:"Jost",sans-serif;color:var(--ink)}
.abs{position:absolute}
.slab{font-family:"Roboto Slab",serif}
.accent{color:var(--orange)}

/* header */
.hero-bg{left:0;top:0;width:1200px;height:664px;background:linear-gradient(90deg,#fff 0%,var(--hero-bg) 55%,#ebeaea 100%)}
.logo{left:102px;top:14px;font-family:"Roboto Slab",serif;font-weight:600;font-size:44px;color:var(--ink);letter-spacing:1px}
.nav{left:377px;top:30px;display:flex;gap:0;font-size:15px;color:#333}
.nav a{position:absolute;white-space:nowrap;color:#333;text-decoration:none}
.nav a.active{color:var(--orange);border-bottom:2px solid var(--orange);padding-bottom:6px}
.btn-outline{border:2px solid var(--orange);color:var(--orange);border-radius:30px;display:flex;align-items:center;justify-content:center;font-size:15px;background:transparent}
.btn-fill{background:linear-gradient(90deg,var(--orange-light),var(--orange-deep));color:#fff;border-radius:30px;display:flex;align-items:center;justify-content:center;font-size:17px;font-weight:500}
.btn-white{border:2px solid #fff;color:#fff;border-radius:30px;display:flex;align-items:center;justify-content:center;font-size:17px}

.hero-title{left:0;width:1200px;top:118px;text-align:center;font-family:"Roboto Slab",serif;font-weight:400;font-size:43px}
.hero-title strong{display:block;color:var(--orange);font-weight:600;font-size:52px;line-height:1.1}
.art{border-radius:24px}

/* section heading */
.h2{font-family:"Roboto Slab",serif;font-weight:400;font-size:44px}
.h2 b{color:var(--orange);font-weight:600}
.rule{height:3px;width:52px;background:var(--orange)}
.para{font-size:14.5px;line-height:24px;color:var(--text)}

.feature-icon{width:75px;height:75px;border-radius:50%;background:var(--orange);display:flex;align-items:center;justify-content:center}
.feature-label{font-size:15px;font-weight:600;line-height:20px;color:#222}

.timeline{left:601px;top:1652px;height:718px;border-left:2px dashed #f4b08b}
.step{width:46px;height:46px;border-radius:50%;background:var(--orange);color:#fff;font-weight:600;font-size:15px;display:flex;align-items:center;justify-content:center}
.item-title{font-family:"Roboto Slab",serif;font-weight:600;font-size:29px;line-height:32px}
.item-title span{color:var(--orange)}

/* band */
.band{left:0;top:2667px;width:1185px;height:576px;background:linear-gradient(90deg,var(--orange-light),var(--orange-deep));border-radius:0 288px 288px 0}
.band-title{left:115px;top:2800px;font-family:"Roboto Slab",serif;color:#fff;font-size:38px;line-height:38px}
.band-title b{font-weight:700}

/* footer */
.footer{left:0;top:3839px;width:1200px;height:383px;background:var(--footer);border-radius:90px 90px 0 0}
.footer-bar{left:0;top:4154px;width:1200px;height:68px;background:var(--footer-bar);color:#9a9a9a;font-size:11px;display:flex;align-items:center;justify-content:center}
.f-head{font-size:19px;color:#fff;font-weight:500}
.f-head::after{content:"";display:block;width:36px;height:2px;background:var(--orange);margin-top:6px}
.f-links{list-style:none;font-size:13px;color:#ddd;line-height:28.5px}
.social{width:28px;height:28px;border-radius:50%;background:#fff}
</style>
</head>
<body>

<!-- Header / hero -->
<div class="abs hero-bg"></div>
<div class="abs logo">Velasto</div>
<nav class="abs nav">
  <a class="active" style="left:0">About Us</a>
  <a style="left:118px">Our Services</a>
  <a style="left:261px">How it work</a>
  <a style="left:397px">Why Us</a>
  <a style="left:502px">Blogs</a>
</nav>
<a class="abs btn-outline" style="left:972px;top:23px;width:123px;height:34px;font-size:14px">Contact Us</a>

<h1 class="abs hero-title">Velasto is here to help<strong>Businesses like yours</strong></h1>
<a class="abs btn-fill" style="left:506px;top:244px;width:179px;height:48px">Get Started</a>
<div class="abs art" role="img" aria-label="Illustration of three colleagues working at a shared office desk with laptops" style="left:254px;top:311px;width:631px;height:468px;background:linear-gradient(180deg,#ebe9e8,#f3d9cb)"></div>

<!-- About -->
<div class="abs art" role="img" aria-label="Illustration of a person working at a desk beneath gears reading Boost Work" style="left:115px;top:877px;width:459px;height:443px;background:radial-gradient(circle at 50% 50%,#fbd3bd,#f3f1f0 70%)"></div>
<h2 class="abs h2" style="left:644px;top:905px">About <b>Velasto</b></h2>
<p class="abs para" style="left:644px;top:990px;width:465px">Lorem Ipsum is simply dummy text of the printing and typesetting industry. Lorem Ipsum has been the industry's standard dummy text ever since the 1500s dummy text of the printing a</p>

<div class="abs feature-icon" style="left:644px;top:1103px">
  <svg width="36" height="36" viewBox="0 0 36 36" fill="none" stroke="#fff" stroke-width="2"><circle cx="12" cy="18" r="6"/><rect x="22" y="6" width="9" height="9"/><rect x="22" y="21" width="9" height="9"/></svg>
</div>
<div class="abs feature-icon" style="left:784px;top:1103px">
  <svg width="36" height="36" viewBox="0 0 36 36" fill="none" stroke="#fff" stroke-width="2"><rect x="5" y="7" width="26" height="23"/><path d="M5 13h26M11 4v6M25 4v6M10 19h4M16 19h4M22 19h4M10 24h4M16 24h4"/></svg>
</div>
<div class="abs feature-icon" style="left:934px;top:1103px">
  <svg width="36" height="36" viewBox="0 0 36 36" fill="none" stroke="#fff" stroke-width="2"><path d="M6 30h26M9 30V22M15 30V18M21 30V20M27 30V13M7 18l8-7 6 5 9-9"/></svg>
</div>
<div class="abs feature-label" style="left:650px;top:1190px">Manage Your<br>Business</div>
<div class="abs feature-label" style="left:793px;top:1190px">Event Manage<br>&amp; Planning</div>
<div class="abs feature-label" style="left:946px;top:1188px">Increase Employee<br>Retention</div>
<a class="abs btn-outline" style="left:641px;top:1262px;width:159px;height:45px">Learn More</a>

<!-- What we do -->
<h2 class="abs h2" style="left:0;width:1212px;text-align:center;top:1448px">What <b>We Do</b></h2>
<div class="abs rule" style="left:580px;top:1509px"></div>

<div class="abs timeline"></div>
<div class="abs step" style="left:579px;top:1629px">01</div>
<div class="abs step" style="left:579px;top:2008px">02</div>
<div class="abs step" style="left:579px;top:2343px">03</div>

<div class="abs item-title" style="right:675px;top:1615px;text-align:right">Increase Employee<br><span>Retention</span></div>
<p class="abs para" style="right:672px;top:1690px;width:380px;text-align:right;line-height:25px;font-size:13.5px">Lorem Ipsum is simply dummy text of the printing and typesetting industry. Lorem Ipsum has been the industry's standard dummy text ever since the 1500s, when an nknown. printer took a galley of type and scrambled</p>
<a class="abs btn-outline" style="left:370px;top:1811px;width:160px;height:45px">Learn More</a>
<div class="abs art" role="img" aria-label="Illustration of a man working at a computer desk with a clock and progress bar" style="left:680px;top:1598px;width:246px;height:246px;background:linear-gradient(160deg,#f5f3f2,#f7cdb4)"></div>

<div class="abs art" role="img" aria-label="Illustration of a large calendar with books, a pencil and a person holding a phone" style="left:246px;top:1959px;width:295px;height:266px;border-radius:50%;background:radial-gradient(circle,#f8c7a8,#efedec 75%)"></div>
<div class="abs item-title" style="left:675px;top:1998px">Easy Event <span>Planning</span></div>
<p class="abs para" style="left:676px;top:2042px;width:390px;line-height:25px;font-size:13.5px">Lorem Ipsum is simply dummy text of the printing and typesetting industry. Lorem Ipsum has been the industry's standard dummy text ever since the 1500s</p>
<a class="abs btn-outline" style="left:677px;top:2139px;width:159px;height:44px">Learn More</a>

<div class="abs item-title" style="right:672px;top:2344px;text-align:right">From Raffles to <span>Auctions</span></div>
<p class="abs para" style="right:666px;top:2397px;width:380px;text-align:right;line-height:25px;font-size:13.5px">Lorem Ipsum is simply dummy text of the printing and typesetting industry. Lorem Ipsum has been the industry's standard dummy text ever since the 1500s</p>
<a class="abs btn-outline" style="left:375px;top:2487px;width:159px;height:44px">Learn More</a>
<div class="abs art" role="img" aria-label="Illustration of a laptop showing bid and ticket tags with a woman seated nearby" style="left:664px;top:2295px;width:349px;height:320px;border-radius:50%;background:radial-gradient(circle,#f6b98f,#f1efee 72%)"></div>

<!-- Orange band -->
<div class="abs band"></div>
<h2 class="abs band-title"><span style="font-weight:300">Boost employee morale</span><br><b>and transform your<br>work events</b></h2>
<p class="abs para" style="left:117px;top:2952px;width:420px;color:#fff;font-size:15.5px;line-height:26px">Lorem Ipsum is simply dummy text of the printing and typesetting industry. Lorem Ipsum has been the industry's standard</p>
<a class="abs btn-white" style="left:113px;top:3052px;width:182px;height:50px">Get Started</a>
<div class="abs art" role="img" aria-label="Illustration of a businessman with a tablet beside a large dashboard screen, plant and shelves" style="left:549px;top:2787px;width:533px;height:336px;background:linear-gradient(135deg,#3b3d44 0%,#3b3d44 45%,#f6f2ee 46%,#ffb487 100%);opacity:.9"></div>

<!-- Start building -->
<div class="abs art" role="img" aria-label="Illustration of a joyful man surrounded by floating event icons and calendars" style="left:98px;top:3328px;width:509px;height:426px;background:radial-gradient(circle at 50% 55%,#fbc6a5,#f4f2f1 70%)"></div>
<h2 class="abs slab" style="left:638px;top:3410px;font-size:40px;font-weight:400;line-height:44px">Start building your<br><span class="accent" style="font-weight:700">event today with me!</span></h2>
<div class="abs rule" style="left:640px;top:3504px;width:50px;height:2px"></div>
<p class="abs para" style="left:636px;top:3526px;width:470px;font-size:14px">Lorem Ipsum is simply dummy text of the printing and typesetting industry. Lorem Ipsum has been the industry's standar</p>
<a class="abs btn-fill" style="left:634px;top:3593px;width:169px;height:44px;font-size:16px">Get Started</a>

<!-- Footer -->
<footer>
  <div class="abs footer"></div>
  <div class="abs logo" style="left:110px;top:3908px;color:#fff">Velasto</div>
  <p class="abs" style="left:112px;top:3983px;width:240px;font-size:13px;line-height:19.5px;color:#bbb">Lorem Ipsum is simply dummy text of the printing and typesetting industry. Lorem Ipsum has been.</p>

  <div class="abs f-head" style="left:462px;top:3912px">Navigation</div>
  <ul class="abs f-links" style="left:465px;top:3950px"><li>About Us</li><li>What We Do</li><li>Our Services</li><li>Why Us</li></ul>

  <div class="abs f-head" style="left:698px;top:3912px">Resources</div>
  <ul class="abs f-links" style="left:702px;top:3950px"><li>Support</li><li>Testimonials</li><li>FAQ</li><li>Contact Us</li></ul>

  <div class="abs f-head" style="left:921px;top:3912px">Stay in touch</div>
  <div class="abs social" style="left:923px;top:3953px;background:var(--orange)"></div>
  <div class="abs social" style="left:956px;top:3953px"></div>
  <div class="abs social" style="left:987px;top:3953px"></div>
  <div class="abs social" style="left:1019px;top:3953px"></div>

  <div class="abs footer-bar">© 2022 velasto. All rights reserved &nbsp;|&nbsp; Privacy &nbsp;|&nbsp; Terms of Use</div>
</footer>

</body>
</html>
```